Deck Forge

We need a logo and website that reflects a platform, enabling for users (consultants and corporate clients) to have for them powerpoint slides produced.
See the mockup in attachment - Look& feel Style www.vornithe.com. See a similar website content (but outdated presentation and to be made more appealing with new modern ways to promote (old website with same proposition: http://www.plumwardenhub.com/). Look and feel wished: www.tindalrope.com (see number that show dynamic evolution) or www.vornithe.com

We have no name - that is part of the mission

```html
<!DOCTYPE html>
<html lang="en">
<head>
<meta charset="utf-8">
<title>Vornithe – Slides for Consultants</title>
<link href="https://fonts.googleapis.com/css2?family=Open+Sans:wght@400;600;700&display=swap" rel="stylesheet">
<style>
:root{
  --blue:#1e6fc4;
  --blue-deep:#0d4f9c;
  --blue-light:#3d8fe0;
  --navy:#0b2f6b;
  --navy-dark:#08224f;
  --ink:#333a44;
  --muted:#7a8190;
  --line:#e3e6ea;
  --white:#ffffff;
  --paper:#f5f6f8;
}
*{box-sizing:border-box;margin:0;padding:0}
html,body{width:736px;height:1200px;overflow:hidden}
body{font-family:"Open Sans",Arial,sans-serif;color:var(--ink);background:var(--white);position:relative}

/* Hero */
.hero{position:absolute;left:0;top:0;width:736px;height:245px;
  background:linear-gradient(115deg,#2a7fd4 0%,#4aa0e8 45%,#1c66b8 100%);overflow:hidden}
.hero-visual{position:absolute;inset:0;
  background:linear-gradient(160deg,rgba(255,255,255,.25) 0%,rgba(255,255,255,0) 55%),
             linear-gradient(180deg,rgba(10,60,130,0) 60%,rgba(10,60,130,.35) 100%)}
.hero-shade{position:absolute;left:0;top:0;width:736px;height:245px}
.site-header{position:absolute;left:0;top:0;width:736px;height:56px;display:flex;align-items:center;padding:0 22px}
.brand{display:flex;align-items:center;gap:7px;color:var(--white);font-weight:700;font-size:17px;letter-spacing:1px}
.brand-dot{width:13px;height:13px;background:var(--white);border-radius:50%}
.main-nav{display:flex;gap:24px;margin-left:64px}
.main-nav a{color:var(--white);text-decoration:none;font-size:9px;font-weight:600;letter-spacing:.4px}
.pilot-btn{position:absolute;right:10px;top:0;background:var(--white);color:var(--ink);
  font-size:10px;font-weight:700;padding:5px 14px;border-radius:0 0 3px 3px}

/* Partner strip */
.partners{position:absolute;left:0;top:245px;width:736px;height:70px;display:flex;
  justify-content:space-around;align-items:center;padding:0 24px;border-bottom:1px solid var(--line)}
.partners span{color:#8b8f96;font-size:13px;font-weight:600;letter-spacing:.5px}

/* Features */
.section-title{position:absolute;left:0;width:736px;text-align:center;font-size:16px;font-weight:700;color:var(--ink)}
.section-title em{font-style:normal;color:var(--blue)}
.features-title{top:343px}
.title-rule{position:absolute;left:343px;width:50px;height:2px;background:var(--blue)}
.features{position:absolute;left:60px;top:385px;width:616px;display:flex;justify-content:space-between}
.feature{width:180px;text-align:center}
.feature-icon{width:42px;height:42px;margin:0 auto 8px;background:var(--blue-deep);border-radius:3px;display:flex;align-items:center;justify-content:center}
.feature h3{font-size:11px;font-weight:700;margin-bottom:6px}
.feature p{font-size:7px;line-height:1.5;color:var(--muted)}

/* Stats */
.stats{position:absolute;left:0;top:545px;width:736px;height:120px;
  background:linear-gradient(90deg,var(--blue-deep),var(--blue) 50%,var(--blue-deep));
  display:flex;justify-content:space-around;align-items:center;color:var(--white);text-align:center}
.stat-label{font-size:11px;font-weight:600}
.stat-value{font-size:28px;font-weight:700;margin:4px 0}
.stat-note{font-size:10px}

/* Work */
.work-title{top:683px}
.gallery{position:absolute;left:0;top:718px;width:736px;height:108px;display:flex}
.gallery div{flex:1}
.pager{position:absolute;left:343px;top:838px;display:flex;gap:10px}
.pager span{width:18px;height:18px;border-radius:50%;border:1px solid var(--line);display:flex;align-items:center;justify-content:center;color:var(--muted);font-size:10px}

/* Footer */
.site-footer{position:absolute;left:0;top:870px;width:736px;height:330px;background:var(--navy);color:var(--white);padding:22px 28px 0}
.footer-cols{display:flex;gap:22px}
.footer-col{flex:1}
.footer-col h4{font-size:11px;font-weight:700;margin-bottom:10px}
.footer-col p{font-size:7.5px;line-height:1.55;margin-bottom:7px;color:#d5def0}
.footer-col p b{color:var(--white)}
.socials{display:flex;gap:6px;margin-top:6px}
.socials span{width:10px;height:10px;border-radius:50%;background:#d5def0}
.field-row{display:flex;gap:6px;margin-bottom:6px}
.field{background:var(--white);color:#999;font-size:7px;padding:5px 6px;border-radius:2px;flex:1}
.field.message{height:44px;margin-bottom:8px}
.send-btn{display:inline-block;background:var(--white);color:var(--navy);font-size:7px;font-weight:700;padding:5px 9px;border-radius:2px}
.map{width:100%;height:105px;background:linear-gradient(135deg,#e8e2d2,#cfdcc4 60%,#b9cfe4);border-radius:2px}
.copyright{position:absolute;left:0;bottom:0;width:736px;height:40px;border-top:1px solid rgba(255,255,255,.15);
  background:var(--navy-dark);font-size:7.5px;text-align:center;line-height:40px;color:#c7d2e6}
</style>
</head>
<body>

<section class="hero">
  <div class="hero-visual" role="img" aria-label="Blue-tinted photo of a workspace with laptop and charts"></div>
  <svg class="hero-shade" viewBox="0 0 736 245" aria-hidden="true">
    <polygon points="0,0 300,0 140,245 0,245" fill="rgba(255,255,255,.12)"/>
  </svg>
  <header class="site-header">
    <div class="brand"><span class="brand-dot"></span>VORNITHE</div>
    <nav class="main-nav">
      <a href="#">OUR VALUE PROPOSITION</a>
      <a href="#">WHO WE ARE</a>
      <a href="#">PRICING</a>
      <a href="#">CONTACT</a>
    </nav>
    <a class="pilot-btn">Free Pilot</a>
  </header>
</section>

<div class="partners">
  <span>Harlow&amp;Pine</span>
  <span>nestly</span>
  <span>Verdane</span>
  <span>NORTHMERE</span>
  <span>CLAY HOUSE</span>
  <span>LUMIERA</span>
</div>

<h2 class="section-title features-title">Partners &amp; <em>Consulting Analysis</em></h2>
<div class="title-rule" style="top:368px"></div>

<div class="features">
  <div class="feature">
    <div class="feature-icon">
      <svg width="20" height="20" viewBox="0 0 20 20"><path d="M4 9h3v8H4zM8 9l3-6c1.5 0 2 1 2 2l-1 3h4c1 0 1.5 1 1.2 2l-1.5 6c-.2.6-.7 1-1.3 1H8z" fill="#fff"/></svg>
    </div>
    <h3>Cost</h3>
    <p>Get polished slides at a fair price with clear rates per deck and no hidden fees for any team or size of project.</p>
  </div>
  <div class="feature">
    <div class="feature-icon">
      <svg width="20" height="20" viewBox="0 0 20 20"><path d="M10 2c3 2 5 5 4 10l-2 2H8l-2-2C5 7 7 4 10 2zM8 15l-2 3 3-1zM12 15l2 3-3-1z" fill="#fff"/><circle cx="10" cy="8" r="1.6" fill="#0d4f9c"/></svg>
    </div>
    <h3>Speed</h3>
    <p>Our network of skilled designers turns your notes into clean decks within hours, so you meet every client deadline with ease.</p>
  </div>
  <div class="feature">
    <div class="feature-icon">
      <svg width="20" height="20" viewBox="0 0 20 20"><circle cx="10" cy="8" r="5" fill="none" stroke="#fff" stroke-width="2"/><path d="M7 12l-2 6 5-2 5 2-2-6" fill="#fff"/></svg>
    </div>
    <h3>Quality</h3>
    <p>Every deck is checked by senior reviewers for layout, charts and tone so your message lands clearly in every boardroom meeting.</p>
  </div>
</div>

<section class="stats">
  <div><div class="stat-label">Countries</div><div class="stat-value">12</div><div class="stat-note">Active</div></div>
  <div><div class="stat-label">Corporate</div><div class="stat-value">145</div><div class="stat-note">Clients served</div></div>
  <div><div class="stat-label">Slides</div><div class="stat-value">20.000</div><div class="stat-note">Produced</div></div>
  <div><div class="stat-label">Free lance</div><div class="stat-value">1540</div><div class="stat-note">Consultants served</div></div>
</section>

<h2 class="section-title work-title">Latest <em>Work</em></h2>
<div class="title-rule" style="top:706px"></div>

<div class="gallery">
  <div role="img" aria-label="Stationery set with paper clips on a desk" style="background:linear-gradient(135deg,#c99a78,#e7c7a8)"></div>
  <div role="img" aria-label="Printed letterhead and business cards" style="background:linear-gradient(135deg,#efeae3,#d9d2c8)"></div>
  <div role="img" aria-label="Folded brochure and notebook" style="background:linear-gradient(135deg,#f2f2ef,#c8c4bd)"></div>
  <div role="img" aria-label="Poster design on a mint background" style="background:linear-gradient(135deg,#8fd4cf,#5cbab5)"></div>
  <div role="img" aria-label="Stacked business cards on pink" style="background:linear-gradient(135deg,#f1c6cc,#e6a9b2)"></div>
  <div role="img" aria-label="Branded mug on a blue background" style="background:linear-gradient(135deg,#9fd2ef,#5bb3e3)"></div>
</div>
<div class="pager"><span>‹</span><span>›</span></div>

<footer class="site-footer">
  <div class="footer-cols">
    <div class="footer-col">
      <h4>Contact Us</h4>
      <p>Please feel free to contact us for any issue. Our staff is available to you from Mon until 5PM on weekdays.</p>
      <p><b>Phone:</b> 555-0142-777</p>
      <p><b>Office:</b> 18 Harbor Lane, Brookfield</p>
      <p><b>Email:</b> info@vornithe.com</p>
      <div class="socials"><span></span><span></span><span></span><span></span><span></span></div>
    </div>
    <div class="footer-col">
      <h4>Feel Free to Mail</h4>
      <div class="field-row"><div class="field">Name*</div><div class="field">Email*</div></div>
      <div class="field message">Write Your Message Here</div>
      <span class="send-btn">SEND MESSAGE</span>
    </div>
    <div class="footer-col">
      <h4>Headquarters</h4>
      <div class="map" role="img" aria-label="Street map showing the office location"></div>
    </div>
    <div class="footer-col">
      <h4>About Team</h4>
      <p>Deck Forge brings together consultants and designers who love clear stories. We help firms of every size turn rough ideas into sharp slides.</p>
      <p>Our team works across time zones to keep your decks moving from draft to final.</p>
    </div>
  </div>
  <div class="copyright">Copyright © Vornithe Consulting All rights reserved</div>
</footer>

</body>
</html>
```